Brise haute coffee - Label design

Watchout: Keep in mind while you submit it needs to be a LABEL (that will be sticked on brown kraft 250 g side gusset coffee pouches). No custom pack for time being (need more scale to custom print pack).

Looking for a label design for my new Doux Vent collection of freshly roasted, single origin specialty coffee. Brand name is Brise Haute (it means red earth and alludes to the soil coffee grows on at high altitude in Africa. It also alludes to the red color of the coffee fruit). Brand selling line is "Pure Origin Coffee". Label to go as stickers on 250 g side gusset coffee pouches in Kraft brown paper (will print labels and stick on packs, packs are 80 mm wide and 260 mm long). This is a relatively complex project comprising the "brise haute" brand logo (funded separately, winner will have the job), the "Doux Vent" collection visual identity, iconic assets for brand and collection recognition across lineup, educational visual icons, text placeholders. It needs to combine hard point visual elements and soft points (text placeholder) which I can easily edit on need basis (text needs to be "outlines" for easy editing after submission). Winner of label submission gets to design brand logo. I will ultimately need 3 different labels for our Doux Vent collection, one for each continent our coffee comes from (Africa, Asia, Latin America). This pitch should focus on the Africa one only. Winner will then have opportunity to design the other ones in consistent way.

BRIEF:
We roast single origin, high quality specialty coffee from high altitude estates in Africa (volcanic slopes in Congo and Burundi, Highlands in Ethiopia and Kenya) Design need to induce the premiumness of the proposition (this is a collection called "Doux Vent"), as well the the unique geographical origins of our coffee (without being too specific as we want to use same label for all our African origins) -oversized shape of continent in background + some visuals conveying the African roots could work well. It needs to create a mental Journey "back to the origins" - of mankind, of unique terroirs creating the best coffee, of our unspoilt roots. So the Journey themes is critical (to be expressed by the telegram type of font, by the way Africa is brought to life,etc.). At the same time keep in mind label space is limited (label stickers go on 250 g coffee pouches made in kraft brown paper) and we want to have a pure design, which leaves room to the text placeholder (see below) and is easily recognizable and reapplicable across the SKUs (we will add Asia and Latin America packs once we lock Africa). As such we need to strike right balance between visual differentiation by origin (Africa, Asia, Latin America) and common iconic assets for brand recognition and lineup harmonization (same font, same way the continent is brought to life, same structure of the label, differentiation by color background,etc.).

We need placeholder for text that will specify exact name of estate, county of origin, coffee type, roasting level and tasting notes. Here I will allow myself some creative direction: it should be in the format of a vintage luggage tag (see attached examples) where we can edit content in Telegram font (our coffee sourcing changes often). We will need to assess if the tag remains standard across collection, or whether we are able to give it a visual twist for each origin (Africa, Asia, Latin America). That would be nicer (see Morvelin "Stamps" example), but priority of the text placeholder is clarity of information above anything else.

Last nice to have (if it time allows) we need educational visual icons (ideally as separate small round labels we can stick on the pack above the main label) for recommended brewing method (filter, espresso, italian moka, french press).

Reason: Still looking for the design in line with brief. Will send feedback to the top 3 routes today.

Target Market(s)

Switzerland

Industry/Entity Type

Coffee Shop

Logo Text

Brise haute -Pure Origin Coffee

Font styles to use
Other font styles liked:
• TELEGRAM type of font to induce geographical journey, single origin,.. For the "luggage tag" placeholder

Requirements
Must have
• - Brand name: Brise Haute. Brand selling line: Pure Origin Coffee. Brand Logo: winner of label submission gets to design brand logo
• - Collection name: DOUX VENT (written, I can see well as a vertical block). name of SKU: AFRICA (visualized a must, written tbc).
• - Text place holder (vintage luggage tag in telegram font) : we will show there name of estate, country of origin, tasting notes. I could see nicely a baggage tag format, where we fill in the details in telegram type of font.
• - 100% single origin Arabica (at the bottom)
• - 250 g (at the bottom)
• Technical Specs:
• A. Artwork must be supplied in either Adobe illustrator or Adobe Photoshop files or Coral Draw files
• B. Create all text in artwork in ‘ outlines ’
• C. The resolution of photographic image files must be no less than 350 dpi
• D. Never flatten the file as we require all layers
• E. All Photoshop image files should be linked and attached. Never flatten the layers and do not change the directory
• F. Create the images with CMYK colour mode ( RGB colour mode is not for printing)
• G. If you are going to use a spot colour please reference the Pantone ( PMS #)
• H. Designate all ‘Transparent’ areas in the artwork with a custom Pantone colour as well as designating the layer’s name as ‘ Transparent’. Please indicate specifically which pantone colour is designated for the ‘transparent’ area.
• I. Reduce any barcodes to 85% as a minimum scale
Nice to have
• - educational simple visual icons on recommended brewing method (filer, italian moka, french press or espresso) as additional small stickers to stick above main label

```html
<!DOCTYPE html>
<html lang="en">
<head>
<meta charset="utf-8">
<title>Brise Haute – Doux Vent Africa label</title>
<link rel="stylesheet" href="https://fonts.googleapis.com/css2?family=Oranienbaum&family=Oswald:wght@300;400;500&family=Courier+Prime&family=Courgette&display=swap">
<style>
  :root {
    --backdrop: #8b8886;
    --kraft: #b48b64;
    --kraft-tag: #c9a27c;
    --paper: #ffffff;
    --rust: #8e3a1d;
    --espresso: #3a2a20;
    --ink: #2e2620;
    --ochre: #f6c77d;
    --map: #fcefdc;
    --tag-line: #6b4a33;
  }
  * { margin: 0; padding: 0; box-sizing: border-box; }
  html, body { width: 1004px; height: 1200px; overflow: hidden; }
  body { background: var(--backdrop); position: relative; font-family: "Oswald", sans-serif; }

  .pouch {
    position: absolute; left: 107px; top: 108px; width: 515px; height: 987px;
    background: var(--kraft);
    box-shadow: 0 6px 14px rgba(0,0,0,.35);
  }
  .brew-sticker {
    position: absolute; left: 32px; top: 35px; width: 77px; height: 77px;
    border-radius: 50%; background: var(--paper); border: 2px solid var(--rust);
    display: flex; flex-direction: column; align-items: center; justify-content: center;
  }
  .brew-sticker svg { width: 30px; height: 26px; margin-top: 4px; }
  .brew-sticker .brew-name { font-family: "Courgette", cursive; font-size: 11px; color: var(--ink); margin-top: 1px; }

  .label {
    position: absolute; left: 44px; top: 271px; width: 419px; height: 646px;
    background: var(--paper); overflow: hidden;
  }
  .continent-map {
    position: absolute; left: 55px; top: 10px; width: 350px; height: 300px;
    background: radial-gradient(ellipse at 50% 45%, var(--map) 0%, var(--map) 55%, rgba(252,239,220,0) 75%);
  }
  .brand-band {
    position: absolute; left: 290px; top: 0; width: 102px; height: 164px;
    background: var(--espresso); border-radius: 0 0 10px 10px;
  }
  .brand-seal {
    position: absolute; left: 6px; top: 28px; width: 90px; height: 90px;
    border-radius: 50%; background: var(--paper);
    display: flex; align-items: center; justify-content: center;
  }
  .brand-seal span { font-family: "Oranienbaum", serif; font-size: 17px; color: var(--rust); }

  .collection { position: absolute; left: 49px; top: 55px; color: var(--rust); }
  .collection-name { font-family: "Oswald", sans-serif; font-weight: 300; font-size: 31px; letter-spacing: 2px; line-height: 1; }
  .collection-word { font-family: "Oswald", sans-serif; font-weight: 400; font-size: 11px; letter-spacing: 7.4px; margin-top: 4px; }

  .title-block { position: absolute; left: 0; top: 232px; width: 100%; text-align: center; }
  .selling-line { font-family: "Oranienbaum", serif; font-size: 36px; color: var(--rust); line-height: 1; }
  .rule { width: 322px; height: 2px; background: var(--rust); margin: 7px auto 0; }
  .rule.thick { height: 3px; margin-top: 4px; }
  .brand-name { font-family: "Oranienbaum", serif; font-size: 70px; color: var(--ink); line-height: 1; margin-top: 2px; }
  .origin-claim { font-family: "Oswald", sans-serif; font-size: 25px; color: var(--ink); margin-top: 10px; letter-spacing: .2px; }

  .heritage-pattern {
    position: absolute; left: 0; top: 433px; width: 100%; height: 172px;
    background: linear-gradient(180deg, #fbd9a2 0%, var(--ochre) 50%, #fbd9a2 100%);
  }
  .weight-bar {
    position: absolute; left: 0; bottom: 0; width: 100%; height: 38px;
    background: var(--rust); color: var(--paper);
    font-family: "Courier Prime", monospace; font-size: 22px;
    text-align: right; padding-right: 30px; line-height: 38px;
  }

  .tag { position: absolute; left: 670px; top: 40px; width: 288px; height: 518px; }
  .tag svg { position: absolute; left: 0; top: 0; }
  .tag-text { position: absolute; color: var(--ink); }
  .tag-header { left: 12px; top: 205px; font-family: "Oswald", sans-serif; font-weight: 500; font-size: 19px; }
  .tag-field { font-family: "Courier Prime", monospace; font-size: 13px; }
  .tag-brand { left: 0; width: 288px; text-align: center; top: 305px; font-family: "Oswald", sans-serif; font-weight: 500; font-size: 54px; line-height: 1; letter-spacing: 1px; }
  .tag-line { left: 0; width: 288px; text-align: center; top: 391px; font-family: "Courier Prime", monospace; font-size: 13px; }
</style>
</head>
<body>

<div class="pouch">
  <div class="brew-sticker" aria-label="Brewing method: espresso">
    <svg viewBox="0 0 30 26">
      <path d="M12 2 q-2 3 0 5 M16 1 q-2 3 0 5" stroke="#3a2a20" stroke-width="1.2" fill="none"/>
      <path d="M5 10 h18 v5 a7 7 0 0 1 -7 7 h-4 a7 7 0 0 1 -7 -7 z" fill="#3a2a20"/>
      <path d="M23 12 a3 3 0 0 1 0 6" stroke="#3a2a20" stroke-width="2" fill="none"/>
      <rect x="3" y="23" width="22" height="2" rx="1" fill="#3a2a20"/>
    </svg>
    <span class="brew-name">espresso</span>
  </div>

  <div class="label">
    <div class="continent-map" role="img" aria-label="Oversized faint outline map of the African continent"></div>

    <div class="brand-band">
      <div class="brand-seal"><span>Brise Haute</span></div>
    </div>

    <div class="collection">
      <div class="collection-name">DOUX VENT</div>
      <div class="collection-word">COLLECTION</div>
    </div>

    <div class="title-block">
      <div class="selling-line">Pure Origin Coffee</div>
      <div class="rule"></div>
      <div class="brand-name">Brise Haute</div>
      <div class="rule thick"></div>
      <div class="origin-claim">100% SINGLE ORIGIN ARABICA</div>
    </div>

    <div class="heritage-pattern" role="img" aria-label="Ochre band of traditional African geometric pattern with tribal motifs"></div>

    <div class="weight-bar">250 g</div>
  </div>
</div>

<div class="tag">
  <svg width="288" height="518" viewBox="0 0 288 518">
    <path d="M143 203 C120 120 128 10 143 8 C158 10 166 120 143 203" fill="none" stroke="#b06a3e" stroke-width="2.5"/>
    <path d="M14 178 H274 L287 191 V504 L274 517 H14 L1 504 V191 Z" fill="#c9a27c"/>
    <g stroke="#6b4a33" stroke-width="1.2" fill="none">
      <line x1="1" y1="241" x2="287" y2="241"/>
      <line x1="1" y1="281" x2="287" y2="281"/>
      <line x1="143" y1="241" x2="143" y2="281"/>
      <line x1="1" y1="423" x2="287" y2="423"/>
      <line x1="1" y1="475" x2="287" y2="475"/>
      <line x1="207" y1="428" x2="207" y2="517"/>
    </g>
    <path d="M202 432 L207 424 L212 432 Z M202 484 L207 476 L212 484 Z" fill="#2e2620"/>
    <circle cx="143" cy="203" r="17" fill="#8e3a1d"/>
    <circle cx="143" cy="203" r="10" fill="#9aa5b0" stroke="#5d6670" stroke-width="2"/>
    <circle cx="143" cy="203" r="5" fill="#c9a27c"/>
    <path d="M200 212 h50 a5 4 0 0 1 0 8 h-50 z M222 212 l-10 -13 h6 l17 13 z M222 220 l-10 13 h6 l17 -13 z M201 212 l-4 -8 h4 l6 8 z" fill="#2e2620"/>
  </svg>
  <div class="tag-text tag-header">DISCOVERY</div>
  <div class="tag-text tag-field" style="left:12px; top:248px;">origin</div>
  <div class="tag-text tag-field" style="left:150px; top:248px;">country</div>
  <div class="tag-text tag-brand">BRISE HAUTE</div>
  <div class="tag-text tag-line">Pure Origin Coffee</div>
  <div class="tag-text tag-field" style="left:16px; top:443px;">Geographical Journey</div>
  <div class="tag-text tag-field" style="left:16px; top:487px;">Character of the brand</div>
</div>

</body>
</html>
```